Business Card Design For Marketing Agnecy LVT

Need business card design for marketing agency.

Dorian Pell
President, CEO
1-555-304-2917
dorian@lumenvaletrewards.net
www.LumenValeTrewards.biz

Back Side:
Boost Sales Using Rewards, Incentives & Giveaways
Get A Free Sample Package

Target Market(s)

B2B

Industry/Entity Type

Marketing

Contact Information for Business Card

Dorian Pell
President, CEO
1-555-304-2917

Back Side:
Get A Free Sample Package

Please note that my current url is OLD DESIGN. I am working on new design and want the business card to match color themes at least on new site. Here is the demo link for new site so you can see the colors I use, etc.

http://pagekilnstudio.example/qx/dorian/lvt_final/index.html

Requirements
Must have
• Please note that my current url is OLD DESIGN. I am working on new design and want the business card to match color themes at least on new site. Here is the demo link for new site so you can see the colors I use, etc.

Nice to have

Should not have

```html
<!DOCTYPE html>
<html lang="en">
<head>
<meta charset="utf-8">
<title>LVT Business Card</title>
<link rel="stylesheet" href="https://fonts.googleapis.com/css2?family=Montserrat:wght@600;700&family=Roboto:wght@400;500;700&display=swap">
<style>
  :root {
    --brand-blue: #2b5a97;
    --card-white: #f2f2f2;
    --ink-dark: #3a3a3a;
    --text-white: #ffffff;
    --text-soft: #e3eaf4;
    --backdrop: #dcdcdc;
  }
  * { margin: 0; padding: 0; box-sizing: border-box; }
  html, body {
    width: 1200px; height: 576px; overflow: hidden;
    background: var(--backdrop);
  }
  .stage { position: relative; width: 1200px; height: 576px; }
  .card {
    position: absolute; top: 138px;
    width: 484px; height: 294px;
    border-radius: 10px; overflow: hidden;
  }
  .logo-name {
    font-family: "Montserrat", sans-serif; font-weight: 700;
    line-height: 1; white-space: nowrap;
  }

  /* Back side */
  .card-back { left: 82px; background: var(--brand-blue); text-align: center; color: var(--text-white); }
  .back-logo {
    position: absolute; top: 34px; left: 0; right: 0;
    font-size: 96px; color: var(--text-white); letter-spacing: -1px;
  }
  .back-company {
    position: absolute; top: 124px; left: 0; right: 0;
    display: flex; flex-direction: column; align-items: center;
    font-family: "Montserrat", sans-serif; font-weight: 700; line-height: 1;
  }
  .back-company .company-main { font-size: 30px; letter-spacing: 1px; }
  .back-company .company-sub {
    font-weight: 600; font-size: 11px; letter-spacing: 3px;
    margin-top: 4px; padding-top: 3px; border-top: 1px solid var(--text-white);
  }
  .offer-banner { position: absolute; left: 62px; top: 194px; width: 360px; height: 52px; }
  .offer-banner svg { position: absolute; inset: 0; }
  .offer-line {
    position: relative; font-family: "Roboto", sans-serif; font-size: 13px;
    color: #2e2e2e; padding-top: 7px;
  }
  .offer-cta {
    position: relative; font-family: "Roboto", sans-serif; font-weight: 700;
    font-size: 13.5px; color: var(--brand-blue); margin-top: 4px;
  }
  .back-url {
    position: absolute; top: 256px; left: 0; right: 0;
    font-family: "Roboto", sans-serif; font-size: 13px; color: var(--text-soft);
  }

  /* Front side */
  .card-front { left: 602px; background: var(--brand-blue); }
  .card-front .panel-shape { position: absolute; inset: 0; }
  .front-logo {
    position: absolute; left: 0; width: 200px; top: 106px;
    text-align: center; font-size: 76px; color: var(--brand-blue); letter-spacing: -1px;
  }
  .front-info { position: absolute; left: 240px; right: 12px; top: 0; bottom: 0; color: var(--text-white); }
  .front-company {
    position: absolute; top: 46px; left: 0;
    display: flex; flex-direction: column; align-items: stretch;
    font-family: "Montserrat", sans-serif; font-weight: 600; line-height: 1;
  }
  .front-company .company-main { font-size: 28px; letter-spacing: 1px; font-weight: 700; }
  .front-company .company-sub {
    font-size: 12px; letter-spacing: 3.5px; text-align: center;
    margin-top: 4px; padding-top: 4px; border-top: 1px solid var(--text-white);
  }
  .person {
    position: absolute; top: 143px; left: 0;
  }
  .person-name {
    font-family: "Montserrat", sans-serif; font-weight: 600;
    font-size: 18px; line-height: 1;
  }
  .person-title { font-family: "Roboto", sans-serif; font-size: 12px; margin-top: 6px; color: var(--text-soft); }
  .contact-list {
    position: absolute; top: 196px; left: 0;
    list-style: none; font-family: "Roboto", sans-serif; font-size: 12.5px; color: var(--text-soft);
  }
  .contact-list li { display: flex; align-items: center; gap: 9px; height: 18.5px; }
  .contact-list svg { width: 10px; height: 10px; flex: none; }
</style>
</head>
<body>
<main class="stage">

  <section class="card card-back" aria-label="Card back">
    <div class="logo-name back-logo">LVT</div>
    <div class="back-company">
      <span class="company-main">LUMEN VALE</span>
      <span class="company-sub">TREWARDS</span>
    </div>
    <div class="offer-banner">
      <svg viewBox="0 0 360 52" preserveAspectRatio="none" aria-hidden="true">
        <polygon points="0,0 360,0 354,40 200,44 180,52 160,44 6,40" fill="#f4f4f4"/>
      </svg>
      <p class="offer-line">Boost Sales Using Rewards, Incentives &amp; Giveaways</p>
      <p class="offer-cta">GET A FREE SAMPLE PACKAGE</p>
    </div>
    <p class="back-url">www.LumenValeTrewards.biz</p>
  </section>

  <section class="card card-front" aria-label="Card front">
    <svg class="panel-shape" viewBox="0 0 484 294" preserveAspectRatio="none" aria-hidden="true">
      <path d="M0,0 H178 C212,60 226,170 190,294 H0 Z" fill="#3a3a3a"/>
      <path d="M0,0 H172 C204,60 216,170 180,294 H0 Z" fill="var(--card-white)"/>
    </svg>
    <div class="logo-name front-logo">LVT</div>
    <div class="front-info">
      <div class="front-company">
        <span class="company-main">LUMEN VALE</span>
        <span class="company-sub">TREWARDS</span>
      </div>
      <div class="person">
        <p class="person-name">Dorian Pell</p>
        <p class="person-title">President, CEO</p>
      </div>
      <ul class="contact-list">
        <li>
          <svg viewBox="0 0 10 10" aria-hidden="true"><path d="M1,3 Q5,0 9,3 L8,4 L6.5,3.5 L6.5,2.8 Q5,2.4 3.5,2.8 L3.5,3.5 L2,4 Z M2.5,5 H7.5 L8.5,9 H1.5 Z" fill="#e3eaf4"/></svg>
          1-555-304-2917
        </li>
        <li>
          <svg viewBox="0 0 10 10" aria-hidden="true"><rect x="0.5" y="2" width="9" height="6.5" fill="#e3eaf4"/><path d="M0.5,2 L5,5.8 L9.5,2" fill="none" stroke="#2b5a97" stroke-width="1"/></svg>
          dorian@lumenvaletrewards.net
        </li>
        <li>
          <svg viewBox="0 0 10 10" aria-hidden="true"><circle cx="5" cy="5" r="4.3" fill="none" stroke="#e3eaf4" stroke-width="1"/><ellipse cx="5" cy="5" rx="1.8" ry="4.3" fill="none" stroke="#e3eaf4" stroke-width="0.8"/><line x1="0.7" y1="5" x2="9.3" y2="5" stroke="#e3eaf4" stroke-width="0.8"/></svg>
          www.LumenValeTrewards.biz
        </li>
      </ul>
    </div>
  </section>

</main>
</body>
</html>
```